KT Design Business Card

I would like a business card similar to this
https://www.artquorra.com/design/8173920
with my info and a picture of my rifle. You can use something like this
https://www.snaplirra.com/pin/381926405572018843/visual-search/?cropSource=6&h=476&w=268&x=12&y=12
or
https://www.snaplirra.com/pin/219604837751093468/

I have a logo, it is a shepperds staff. I build custom rifles and do Law Enforcement sales. Some where on the card it needs to say something like, "Custom AR's built correctly", "All rifles come with honed uppers and bedded barrels", "All rifles are fully tested and come with a 3 shot card", "Law Enforcement models are available", "Tactical Equipment Consulting", "One stop shop for all tactical equipment"

Business Name: KT Design LLC
Name: Brent Hollis
Phone: (555) 614-2980
Email: brent.ktdesign@mailbriq.com
Address: 3082 Tamblin Ct., Rock Hill, SC, 29815

Just use the concept of the staff in the attachments the other stuff is not related

```html
<!DOCTYPE html>
<html lang="en">
<head>
<meta charset="utf-8">
<title>KT Design Business Card</title>
<link rel="stylesheet" href="https://fonts.googleapis.com/css2?family=Cabin:wght@700&family=Roboto+Condensed:wght@400&display=swap">
<style>
  :root {
    --card-bg: #323033;
    --band: #424242;
    --accent: #f0962a;
    --shadow: rgba(0, 0, 0, 0.55);
  }
  html, body {
    margin: 0;
    padding: 0;
    overflow: hidden;
    background: var(--card-bg);
  }
  .card {
    position: relative;
    width: 1200px;
    height: 720px;
    background: var(--card-bg);
    overflow: hidden;
    color: var(--accent);
  }
  .card__bands {
    position: absolute;
    inset: 0;
  }
  .card__bands polygon {
    fill: var(--band);
  }
  .logo-mark {
    position: absolute;
    left: 474px;
    top: 100px;
    width: 200px;
    height: 200px;
  }
  .logo-mark circle {
    fill: none;
    stroke: var(--accent);
    stroke-width: 14;
  }
  .brand-name {
    position: absolute;
    left: 0;
    width: 1140px;
    top: 330px;
    margin: 0;
    text-align: center;
    font-family: "Cabin", sans-serif;
    font-weight: 700;
    font-size: 66px;
    line-height: 66px;
    letter-spacing: 1px;
    text-shadow: 3px 3px 2px var(--shadow);
  }
  .rifle-marking {
    position: absolute;
    left: 0;
    width: 1140px;
    top: 420px;
    margin: 0;
    text-align: center;
    font-family: "Roboto Condensed", sans-serif;
    font-weight: 400;
    font-size: 41px;
    line-height: 44px;
    text-shadow: 3px 3px 2px var(--shadow);
  }
  .rifle-marking span {
    display: block;
  }
</style>
</head>
<body>
  <main class="card">
    <svg class="card__bands" width="1200" height="720" viewBox="0 0 1200 720" aria-hidden="true">
      <polygon points="848,0 1200,0 1200,459"/>
      <polygon points="0,261 352,720 0,720"/>
    </svg>

    <svg class="logo-mark" viewBox="0 0 200 200" role="img" aria-label="KT Design shepherd's staff logo mark">
      <circle cx="100" cy="100" r="80"/>
    </svg>

    <h1 class="brand-name">KT DESIGN</h1>

    <p class="rifle-marking">
      <span>KTD 15</span>
      <span>MULTI CAL</span>
      <span>S/N: XXXXX</span>
    </p>
  </main>
</body>
</html>
```